Top Construction Software Co Needs a New Magazine Ad Design for 2013

Founded in 1986, BRVT is the market leader for innovative software solutions for the heavy civil construction industry. Our suite of products, including the bestsellers CrestQuote® and CrestTask®, are used by more than 40,000 workers every day to improve their proficiency at estimating, job management, resource management, safety and equipment maintenance. BRVT also offers new mobile applications and cloud computing services so companies can work on a wide array of devices including laptops, tablets and smartphones.

In addition to high quality software, BRVT is best known for providing world-class customer service, and for its friendly, employee-ownership culture. We offer a full range of professional support options to help customers maximize their software investment including implementation planning, training and INSTANT 24/7 phone support.

Project description

We are creating a new magazine ad campaign for 2013 and need a full page and 1/3 page ad for this campaign.

The ad concept is Work Smarter, and we will provide 1 tip in each ad along with a case study of how a construction company can work smarter this year to save money, be more efficient or profitable.

Each ad will feature a "Work Smarter Tip # xx" headline, a sub-heading that contains the actual tip, a construction image that relates to the tip, a case study with bullet points about a company that has done the tip successfully and the results, an offer to download a free report with all of our 40 Work Smarter tips from a landing page, and our logo with branding elements.

The ad will typically run as a 1/3 page ad approximately 4" x 5", but we would like both a full page and 1/3 page design for the ad.

BRVT Brand personality traits - Innovative, market leader, competent, professional, masculine, friendly, and helpful. We've been in business for 27 years, and we are known for our world-class customer support and friendly helpful employees.
Updates

I've added a new logo file that has a square logo and a horizontal logo.  You can use either in the ad.

The text in the case study is a little long, and everyone seems to have a little trouble fitting it in the design.  Feel free to cut the last 2 or 3 bullets in your design, and I will make the text work with the size you give me.

Target Market(s)

Construction company executives, estimators, project managers, equipment managers, and IT support. We mainly target US and Canadian customers.

Industry/Entity Type

Construction

Requirements
Must have
• Ad title- "Work Smarter Tip #6"
Tip- Replace paper timecards with easy mobile apps
Image- Construction image related to the tip. Would like the tip potentially on the image, but open to suggestions. Just need the ad to be eye-catching to readers.
Case Study - Provide a case study of a company that implemented the tip with their results. This needs to be easy to read, and stand out from the ad.
Logo - Must use our company logo and it should be very visible.
Free Report - Want a strong call-to-action offer for the free report. See the attached word document for the copywriting for the ad elements.
Very important - the ad must be eye-catching. Something that will make readers want to read the tip while breezing through a magazine, while still being professional and matching our branding elements. Call to Action for free report should also be very visible.

Brand colors - Green PMS 356 and black are our dominant colors, can use yellow and orange (C=0, M=48, Y=98, K=0) as accent colors.
Nice to have
• We want to be viewed as helpful, industry leader, professional.

I attached a .pdf document of an ad created by a graphic designer that is good, but we are willing to pay to get more creative designs. The .pdf shows basically what we are looking for, but would like more creativity and something that will stop readers. Also, the designer changed our logo which we don't like so use the attached logo.
Should not have
• Feminine design - our industry is largely male construction workers.

Don't use script or goofy fonts
Don't change the logo, or put it in an image where it is not easily viewable.
Don't do something that is unprofessional like show a naked woman, etc.

```html
<!DOCTYPE html>
<html lang="en">
<head>
<meta charset="utf-8">
<title>Work Smarter – Tip #6</title>
<link href="https://fonts.googleapis.com/css2?family=Roboto+Condensed:wght@400;700&family=Roboto:wght@400;700&display=swap" rel="stylesheet">
<style>
  :root{
    --green:#1a9a48;
    --orange:#f7851c;
    --ink:#1d1d1d;
    --gray-band:#5d5f60;
    --panel:#e9eaea;
    --dark:#262727;
    --white:#ffffff;
  }
  *{margin:0;padding:0;box-sizing:border-box}
  html,body{width:849px;height:1200px;overflow:hidden;background:var(--white)}
  .ad{position:relative;width:849px;height:1200px;overflow:hidden;font-family:"Roboto",Arial,sans-serif;color:var(--ink)}
  .hero{position:absolute;left:0;top:0;width:849px;height:585px;
    background:linear-gradient(180deg,#cfe0ee 0%,#b8cfe2 30%,#c9c6b8 48%,#8f9a6a 62%,#6f7c4c 80%,#5b6445 100%)}
  .hero-figure{position:absolute;right:0;top:150px;width:520px;height:435px;
    background:radial-gradient(ellipse at 60% 55%,#b98a60 0%,#d9773a 30%,#8c8f93 60%,rgba(120,130,120,0) 78%)}
  .headline{position:absolute;left:0;top:0;width:849px;height:165px;padding:28px 0 0 42px;
    background:linear-gradient(180deg,rgba(255,255,255,.96) 0%,rgba(255,255,255,.9) 70%,rgba(255,255,255,0) 100%)}
  .tip-label{font-family:"Roboto Condensed",Arial,sans-serif;font-weight:700;font-size:38px;letter-spacing:2px;color:var(--orange);line-height:1}
  .tip-text{font-family:"Roboto Condensed",Arial,sans-serif;font-size:37px;line-height:1.12;color:var(--green);margin-top:12px}
  .case-title{position:absolute;left:0;top:585px;width:849px;height:58px;background:var(--orange);
    font-family:"Roboto Condensed",Arial,sans-serif;font-size:38px;color:var(--white);padding:6px 0 0 30px}
  .case-company{position:absolute;left:0;top:643px;width:849px;height:62px;background:var(--gray-band);
    font-size:25px;color:var(--white);padding:16px 0 0 30px}
  .case-body{position:absolute;left:0;top:705px;width:849px;height:272px;background:var(--panel);padding:12px 100px 0 70px}
  .case-body ul{list-style:none}
  .case-body li{position:relative;font-size:20px;line-height:22px;margin-bottom:2px}
  .case-body li::before{content:"";position:absolute;left:-16px;top:9px;width:5px;height:5px;border-radius:50%;background:var(--ink)}
  .footer{position:absolute;left:0;top:977px;width:849px;height:223px;
    background:linear-gradient(100deg,#f2f2f2 0%,#d9d9d9 42%,#3b3c3c 52%,var(--dark) 100%)}
  .brand{position:absolute;left:90px;top:80px;display:flex;align-items:center;gap:14px}
  .brand-square{width:30px;height:30px;background:var(--green)}
  .brand-name{font-family:"Roboto",Arial,sans-serif;font-weight:400;font-size:48px;color:var(--green);line-height:1}
  .offer{position:absolute;left:560px;top:34px;width:270px;color:var(--white);font-size:19px;line-height:24px}
  .offer p+p{margin-top:18px}
  .offer-url{position:absolute;left:560px;top:186px;color:var(--white);font-size:19px;font-weight:700}
</style>
</head>
<body>
<div class="ad">
  <div class="hero" role="img" aria-label="Photo of a construction foreman in a hard hat and safety vest using a tablet on a paving site"></div>
  <div class="hero-figure" role="img" aria-label="Foreman holding a tablet in the field"></div>

  <header class="headline">
    <div class="tip-label">WORK SMARTER - TIP #6</div>
    <div class="tip-text">Replace your paper timecards<br>with easy mobile apps</div>
  </header>

  <div class="case-title">Case Study:</div>
  <div class="case-company">Hallbrook Construction, an asphalt paving company in Brookdale KS</div>

  <section class="case-body">
    <ul>
      <li>Wanted to be able to monitor job profitability and make the office more efficient.</li>
      <li>Implemented CrestTask® Mobile Apps in the field on tablets.</li>
      <li>Foremen were initially resistant until they tried it, they realized the apps were easy to learn and use.</li>
      <li>Eliminated double-entry of data, lost timecards, unreadable printing</li>
      <li>Now able to see if a job is over-running or under-running right away</li>
      <li>Receive timecards daily instead of weekly</li>
      <li>Reduced payroll time from 2 – 3 days to ½ a day</li>
    </ul>
  </section>

  <footer class="footer">
    <div class="brand"><span class="brand-square"></span><span class="brand-name">BRVT</span></div>
    <div class="offer">
      <p>Free Report -<br>40 Tips for Working Smarter</p>
      <p>Download a free report with 40 tips, case studies, and how-to guides.</p>
    </div>
    <div class="offer-url">www.brvt-demo.com/worksmart</div>
  </footer>
</div>
</body>
</html>
```